Kinderbuchautor sucht emotionales Webdesign
Zielgruppe
Ich bin Autor von Kinderbüchern und suche jemanden,d er meine Website 'Kind- und Elterngerecht' gestalten kann und hier vielleicht gute Ideen oder bestenfalls schon Erfahrung hat.
Ich habe vor ein paar Jahren begonnen, Kinderbücher zu schreiben. Meine Bücher konzentrieren sich auf Kinder zwischen 0 und 12 Jahren. Ich schreibe auf Deutsch und auf Englisch und arbeite mit verschiedenen internationalen Illustratoren zusammen, mit denen ich immer neue Konzepte entwickele.
Formate sind u.a.
- Bilderbücher in verschiedenen Sprachen (insbes. Deutsch und Englisch, aber auch Spanisch, französisch und z.T. Chinesisch)
- Bilinguale Bilderbücher und Erstlese-Bücher (diese sind in der Tat zweisprachig)
- Romane für 8-12 jährige
- einsprachige Erstlese-Bücher
- Chapter Books (zwischen 60 und 100 Seiten)
Mit meinen Geschichten bin ich in erster Linie daran interessiert, neue Erfahrungen zu vermitteln und Anregungen für neue Perspektiven auf die Welt zu geben. Ich möchte das auf spielerische Weise tun, allerdings nicht zufällig. Das Schreiben aus der Perspektive der Kinder öffnet die Tür zu Welten, die von Elfen und Tieren, Meerjungfrauen und Königen, Zwergen und Riesen bevölkert sind – Wesen, die Probleme haben und sie lösen können, indem sie einfach die Beschränkungen unserer realen Welt umgehen. Das Mögliche zu entdecken, wo nichts wahrscheinlich erscheint.
Die Zielgruppe sind in erster Linie Eltern, Großeltern, Lehrer, Pädagogen etc.
Aufgabenstellung
Es geht bei dieser Website insbesondere darum, die richtige Emotion rüber zu bringen. Da viele Bücher zweisprachig sind oder die Bücher in verschiedenen Sprachen veröffentlicht werden, kann auch der Lerncharakter herausgestellt werden. Ich will allerdings nicht, dass die Website mit Lernhilfen für Pädagogen gespickt ist das ist nicht das Ziel. Das ganze soll den Fun-Faktor unterstreichen. Zum Beispiel gibt es in den USA fast eine große Anzahl von sog. 'Home-Learning' Initiativen, bei denen Kinder schon sehr früh mit. z.B. Hilfe von Bilderbüchern und leichten Erstlesebüchern andere Sprachen lernen, das ganze aber nicht als Lernprogramm sehen. Das ist einfach so, weil die Eltern aus zwei verschiedenen Kulturkreisen kommen. Das ist noch weitgehend eine Nische.
Aus diesem Grund werden die Bücher auch im internationalen Bereich, z.B. USA, Kanada, Spanien, Australien und UK vermarktet, neben D-A-CH.
Es gibt bereits eine Website, die aber NICHT als Vorlage genommen werden soll. Hier kann sich an den FARBEN orientiert werden: www.tamrelfisk.example.
DIe Website wurde mit QUMBA erstellt. QUMBA ist aber keine zwingende Vorgabe. Es geht darum, die richtige Emotion zu kreieren.
Beipiele von Seiten, die mir hier gut gefallen, weil sie auch Social-Media optimiert sind, sind z.B. die folgenden:
http://vosterma.example/
https://www.morwenhadley.example/
http://www.gereonswalt.example/
Ich habe ein Logo, das ist ein Name 'Tamr Elfisk' mit der Schrift Luna Bar. Ich habe Illustrationen und Fotos sowie Cover der Bücher als Attachment beigefügt.

```html
<!DOCTYPE html>
<html lang="de">
<head>
<meta charset="utf-8">
<title>Tamr Elfisk – Kinderbücher</title>
<link rel="stylesheet" href="https://fonts.googleapis.com/css2?family=Open+Sans:wght@400;600;700;800&family=Reenie+Beanie&display=swap">
<style>
  :root {
    --red: #e8262b;
    --ink: #1d1d1d;
    --grey: #8a8a8a;
    --line: #e4e4e4;
    --page: #ffffff;
  }
  * { box-sizing: border-box; margin: 0; padding: 0; }
  html, body { width: 1200px; height: 800px; overflow: hidden; background: var(--page); }
  body { font-family: "Open Sans", Arial, sans-serif; color: var(--ink); position: relative; }

  .site-header {
    position: absolute; left: 246px; top: 18px; width: 706px; height: 40px;
    display: flex; align-items: center; justify-content: space-between;
  }
  .brand { font-size: 22px; font-weight: 600; color: var(--ink); letter-spacing: .5px; }
  .main-nav { display: flex; align-items: center; gap: 6px; font-size: 9px; font-weight: 800; letter-spacing: .6px; }
  .main-nav a { color: var(--ink); text-decoration: none; }
  .main-nav a.is-active, .main-nav .lang { color: var(--red); }
  .main-nav .sep { color: var(--red); font-weight: 400; }
  .social-square { width: 11px; height: 11px; background: var(--ink); display: inline-block; }

  .news-head {
    position: absolute; left: 246px; top: 86px; width: 706px;
    display: flex; justify-content: space-between; align-items: center;
  }
  .news-title { font-family: "Reenie Beanie", cursive; font-size: 38px; color: var(--red); font-weight: 400; }
  .slider-dots { display: flex; gap: 5px; margin-right: 345px; }
  .slider-dots span { width: 6px; height: 6px; border-radius: 50%; background: #c9c9c9; }
  .slider-dots span.is-current { background: var(--red); box-shadow: 0 0 0 2px #fff, 0 0 0 3px var(--red); }

  .feature-media { position: absolute; top: 131px; height: 263px; }
  .media-reading { left: 246px; width: 343px; background: linear-gradient(160deg, #cdb48d 0%, #b98f5f 55%, #8d6a45 100%); }
  .media-author { left: 608px; width: 340px; background: linear-gradient(180deg, #f3f1e8 0%, #c8d59a 35%, #2a2523 70%, #c9262a 100%); }

  .date-badge {
    position: absolute; left: 381px; top: 319px; width: 76px; height: 76px; border-radius: 50%;
    background: var(--red); color: #fff; text-align: center; border: 3px solid #fff;
    display: flex; flex-direction: column; justify-content: center; line-height: 1;
  }
  .date-badge .month { font-size: 8px; font-weight: 700; letter-spacing: .5px; }
  .date-badge .day { font-size: 30px; font-weight: 800; }
  .date-badge .year { font-size: 8px; font-weight: 700; }

  .post { position: absolute; left: 254px; top: 402px; width: 690px; }
  .post-title { font-size: 12px; font-weight: 700; color: var(--red); margin-bottom: 6px; }
  .post-text { font-size: 9.5px; line-height: 13px; color: #555; margin-bottom: 9px; }

  .post-meta {
    position: absolute; left: 254px; top: 506px; width: 692px; height: 26px;
    display: flex; align-items: center; gap: 10px; font-size: 8px; color: var(--grey);
    border-bottom: 1px solid var(--line);
  }
  .share { display: flex; gap: 5px; margin-right: 10px; }
  .share span { width: 18px; height: 18px; background: var(--red); }
  .meta-icon { width: 12px; height: 12px; border-radius: 50%; border: 1.5px solid var(--grey); display: inline-block; vertical-align: middle; margin-right: 3px; }
  .meta-item b { color: var(--ink); font-weight: 600; }
  .more-button {
    margin-left: auto; background: var(--red); color: #fff; font-weight: 700; font-size: 8px;
    letter-spacing: 1px; padding: 5px 30px; border-radius: 8px 2px 10px 3px; text-decoration: none;
  }

  .teaser-media { position: absolute; top: 570px; height: 260px; }
  .media-box { left: 246px; width: 343px; background: linear-gradient(180deg, #d8c7a4 0%, #8a5a3c 45%, #c9ab82 100%); }
  .media-books { left: 608px; width: 340px; background: linear-gradient(90deg, #fbe9e0 0%, #f0803a 30%, #f6c3a0 55%, #ea3f8f 80%, #fbe9ef 100%); }
</style>
</head>
<body>
  <header class="site-header">
    <div class="brand">Tamr Elfisk</div>
    <nav class="main-nav">
      <a class="is-active" href="#">HOME</a><span class="sep">|</span>
      <a href="#">ÜBER MICH</a><span class="sep">|</span>
      <a href="#">BÜCHER</a><span class="sep">|</span>
      <a href="#">GRATIS!</a><span class="sep">|</span>
      <a href="#">BLOG</a><span class="sep">|</span>
      <a href="#">KONTAKT</a><span class="sep">|</span>
      <span class="lang">DE</span>
      <span class="social-square"></span>
      <span class="social-square"></span>
    </nav>
  </header>

  <div class="news-head">
    <h2 class="news-title">News of the month..</h2>
    <div class="slider-dots"><span class="is-current"></span><span></span><span></span><span></span></div>
  </div>

  <div class="feature-media media-reading" role="img" aria-label="Foto: Frau liest ein Buch auf einer sonnigen Wiese, neben ihr ein Bücherstapel"></div>
  <div class="feature-media media-author" role="img" aria-label="Foto des Autors mit Clownsnase vor einer Illustration mit Fuchs und Dachs"></div>

  <div class="date-badge"><span class="month">MARCH</span><span class="day">13</span><span class="year">2016</span></div>

  <article class="post">
    <h3 class="post-title">LOREM IPSUM DOLOR SIT AMET, CONSECTETUR ADIPISCING ELIT</h3>
    <p class="post-text">Heute erscheint mein neues Bilderbuch auf Deutsch und Englisch. Ein Abenteuer mit Fuchs und Dachs, das Kinder zum Lachen bringt und Eltern zum Vorlesen einlädt. Ab sofort im Buchhandel erhältlich.</p>
    <p class="post-text">Zur Premiere gibt es eine Lesung mit Musik, Malaktion und Überraschungen für kleine und große Gäste. Wir freuen uns auf euch und auf viele neugierige Fragen rund um Elfen, Tiere und Riesen.</p>
  </article>

  <div class="post-meta">
    <div class="share"><span></span><span></span><span></span><span></span></div>
    <span class="meta-item"><i class="meta-icon"></i>by <b>JohnDoe</b> on June 02, 2016</span>
    <span class="meta-item"><i class="meta-icon"></i>6 comments</span>
    <a class="more-button" href="#">MEHR INFO</a>
  </div>

  <div class="teaser-media media-box" role="img" aria-label="Foto: Kind in einem Pappkarton"></div>
  <div class="teaser-media media-books" role="img" aria-label="Foto: bunte Kinderbücher in Orange und Pink"></div>
</body>
</html>
```